Business Card Design

We need a Business card design for our Family Dental Clinic.
Colour choices - White, blue and golden to go with the logo.
Industry/Entity Type
Business
Contact Information for Business Card
Side 1
DR MONA PELLINGHAM
BDS
Suite 6, Level 2, 418 Wexbridge Street
Fernvale Heights, VIC 3187
Fax : 9476 2035
Email: info@fernvaledentalgroup.com.au
Website: fernvaledentalgroup.com.au
Phone(image) - 9476 2035 (bigger size)
Please make sure that you produce 3 files with the same design
1) As per above
2) With out the Name ( i. e DR Mona Pellingham BDS)
3) Just the card template (no texts)
Side 2
......................................... at ........................
Please give 24 hours notice if you cannot keep this appointment

```html
<!DOCTYPE html>
<html lang="en">
<head>
<meta charset="utf-8">
<title>Fernvale Dental Group – Business Card</title>
<link href="https://fonts.googleapis.com/css2?family=Tinos:wght@400;700&display=swap" rel="stylesheet">
<style>
  :root {
    --page: #ffffff;
    --gold-bright: #fcd54a;
    --gold-pale: #fcf6d6;
    --gold-mid: #e6cf94;
    --gold-deep: #c9a14e;
    --ink: #1d1d1d;
    --brand-blue: #1f8fd6;
    --icon-blue: #19aee8;
  }
  html, body {
    margin: 0;
    width: 1200px;
    height: 1000px;
    overflow: hidden;
    background: var(--page);
  }
  .canvas {
    position: relative;
    width: 1200px;
    height: 1000px;
    font-family: "Tinos", "Times New Roman", serif;
    color: var(--ink);
  }
  .card {
    position: absolute;
    left: 262px;
    width: 752px;
    height: 466px;
    background: linear-gradient(90deg,
      var(--gold-bright) 0%,
      #fbe9a2 12%,
      var(--gold-pale) 25%,
      var(--gold-mid) 42%,
      var(--gold-deep) 60%,
      #dcc07a 75%,
      var(--gold-pale) 100%);
    overflow: hidden;
  }
  .card--front { top: 17px; }
  .card--back { top: 504px; width: 753px; }

  .brand {
    position: absolute;
    display: flex;
    align-items: center;
    gap: 8px;
    color: var(--brand-blue);
    font-weight: 400;
    white-space: nowrap;
  }
  .brand__dot {
    border-radius: 50%;
    background: var(--brand-blue);
    flex: none;
  }
  .brand--large { left: 478px; top: 140px; font-size: 23px; }
  .brand--large .brand__dot { width: 14px; height: 14px; }
  .brand--small { left: 552px; top: 374px; font-size: 12.5px; gap: 5px; }
  .brand--small .brand__dot { width: 8px; height: 8px; }

  .contact {
    position: absolute;
    left: 48px;
    top: 207px;
    font-size: 20.5px;
    line-height: 31.5px;
  }
  .contact p { margin: 0; white-space: nowrap; }
  .phone {
    position: absolute;
    left: 46px;
    top: 366px;
    display: flex;
    align-items: center;
    gap: 7px;
    font-weight: 700;
    font-size: 31px;
  }
  .phone svg { display: block; }

  .appointment {
    position: absolute;
    left: 50px;
    top: 163px;
    width: 690px;
    font-weight: 700;
    font-size: 21.2px;
    line-height: 31px;
  }
  .appointment p { margin: 0; white-space: nowrap; }
</style>
</head>
<body>
<div class="canvas">

  <section class="card card--front">
    <div class="brand brand--large">
      <span class="brand__dot"></span>
      <span class="brand__name">Fernvale Dental Group</span>
    </div>

    <div class="contact">
      <p>BDS Suite 6, Level 2,</p>
      <p>418 Wexbridge Street Fernvale Heights, VIC 3187</p>
      <p>Fax : 9476 2035</p>
      <p>Email: info@fernvaledentalgroup.com.au</p>
      <p>Website: fernvaledentalgroup.com.au</p>
    </div>

    <div class="phone">
      <svg width="23" height="23" viewBox="0 0 23 23" aria-hidden="true">
        <rect width="23" height="23" rx="4" fill="var(--icon-blue)"/>
        <path d="M8 4.5c.8-.4 1.5 0 1.8.7l1 2.4c.2.6 0 1.2-.5 1.5l-1 .6c.5 1.8 1.6 3.5 3.2 4.7l1-.7c.5-.3 1.1-.3 1.5.1l1.9 1.8c.5.5.5 1.3-.1 1.8l-1.1.9c-.8.6-1.9.7-2.8.2C8.8 16.5 6.3 12.6 6 8.2c0-1 .4-2 1.2-2.6z" fill="#ffffff"/>
      </svg>
      <span>9476 2035</span>
    </div>
  </section>

  <section class="card card--back">
    <div class="appointment">
      <p>&nbsp;........................................ at ....................... ......................................... at</p>
      <p>....................... ......................................... at ....................... .........................</p>
      <p>at ........................</p>
      <p>Please give 24 hours notice if you cannot keep this appointment</p>
    </div>

    <div class="brand brand--small">
      <span class="brand__dot"></span>
      <span class="brand__name">Fernvale Dental Group</span>
    </div>
  </section>

</div>
</body>
</html>
```